Resort Room Letter to go in Welcome Basket

It needs the Resort Logo and a snazzier font. Probably some kind of background. It will be in full color. Dimensions 5.5in x 8in. This is the in room letter that goes with the welcome basket.

Text:

Welcome to The Resort! We have prepared this convenient Starter Pack to enhance your stay in our Luxury Condominiums. To further enhance your stay housekeeping will provide daily limited service which includes fresh towels and trash removal. Additional housekeeping services can be scheduled with the front desk for a nominal fee. Please leave the basket so that we can prepare a Starter Pack for the next guest. When you are ready to checkout simply dial **47.

Helpful Hints:

Turn the lever in the freezer to start making ice
The Waterpark can be accessed from the 1st Floor
The Indoor Waterpark is open from 9AM to 11PM
Vending with Snacks & Drinks are available on Floors 1, 2, 4, & 5
The closest grocery store is Brindlemart
You can also conveniently order groceries via Pantrygo from Halvey, Grain Town, & Tamrel
Additional convenience items are available for purchase at the Front Desk
Use our Express Checkout by Dialing **47

Thank you so much for choosing the Resort for your Smoky Mountain Vacation!

The Resort Management Team

```html
<!DOCTYPE html>
<html lang="en">
<head>
<meta charset="utf-8">
<title>Welcome to The Resort – Room Letter</title>
<link rel="stylesheet" href="https://fonts.googleapis.com/css2?family=Great+Vibes&family=Montserrat:wght@400;600;700&display=swap">
<style>
  :root {
    --page: #f2efe9;
    --teal: #1f9c8a;
    --teal-deep: #17806f;
    --gold: #e0a43a;
    --gold-deep: #b97d1f;
    --ink: #ffffff;
    --ink-soft: #e4f4f1;
    --shadow: rgba(0,0,0,0.18);
  }
  * { box-sizing: border-box; margin: 0; padding: 0; }
  html, body { width: 1200px; height: 851px; overflow: hidden; background: var(--page); }
  body { font-family: "Montserrat", sans-serif; color: var(--ink); }

  .letter {
    position: absolute; left: 325px; top: 25px;
    width: 550px; height: 800px;
    background: var(--teal);
    box-shadow: 0 6px 20px var(--shadow);
    overflow: hidden;
  }
  .hanger-hole { position: absolute; left: 0; top: 0; }

  .greeting {
    position: absolute; left: 30px; top: 70px; width: 170px;
  }
  .greeting__script {
    font-family: "Great Vibes", cursive;
    font-size: 54px; line-height: 1; color: var(--gold);
  }
  .greeting__line {
    font-size: 14px; font-weight: 600; margin-top: 4px; color: var(--ink);
  }
  .brand {
    margin-top: 18px; display: flex; align-items: center; gap: 8px;
  }
  .brand__mark { width: 18px; height: 18px; background: var(--gold); border-radius: 50%; }
  .brand__name { font-size: 16px; font-weight: 700; letter-spacing: 2px; color: var(--gold); }

  .intro {
    position: absolute; left: 210px; top: 30px; width: 310px; height: 250px;
    border: 2px solid var(--ink); padding: 16px 16px;
    font-size: 10.5px; line-height: 1.55; color: var(--ink-soft);
  }

  .hints { position: absolute; left: 30px; top: 300px; width: 490px; }
  .hints__title { font-size: 14px; font-weight: 700; color: var(--gold); margin-bottom: 12px; }
  .hints__list { list-style: none; }
  .hint {
    display: flex; align-items: flex-start; gap: 12px;
    font-size: 11.5px; line-height: 1.45; margin-bottom: 11px; color: var(--ink);
  }
  .hint svg { flex: 0 0 16px; margin-top: 1px; }

  .closing { position: absolute; left: 30px; top: 685px; width: 380px; }
  .closing__thanks { font-size: 12px; font-weight: 600; line-height: 1.5; }
  .closing__team { font-size: 12px; font-weight: 700; color: var(--gold); margin-top: 10px; }

  .corner-brand {
    position: absolute; right: 28px; bottom: 36px;
    display: flex; align-items: center; gap: 6px;
  }
  .corner-brand__mark { width: 12px; height: 12px; background: var(--gold); border-radius: 50%; }
  .corner-brand__name { font-size: 11px; font-weight: 700; letter-spacing: 1.5px; color: var(--gold); }
</style>
</head>
<body>
<article class="letter">
  <svg class="hanger-hole" width="90" height="70" viewBox="0 0 90 70" aria-hidden="true">
    <path d="M30 0 H70 A25 25 0 0 1 45 40 A14 14 0 1 0 45 12 Z" fill="var(--ink)" opacity="0.95"/>
  </svg>

  <header class="greeting">
    <div class="greeting__script">Welcome</div>
    <div class="greeting__line">to The Resort!</div>
    <div class="brand"><span class="brand__mark"></span><span class="brand__name">THE RESORT</span></div>
  </header>

  <p class="intro">
    We have prepared this convenient Starter Pack to enhance your stay in our Luxury Condominiums. To further enhance your stay housekeeping will provide daily limited service which includes fresh towels and trash removal. Additional housekeeping services can be scheduled with the front desk for a nominal fee. Please leave the basket so that we can prepare a Starter Pack for the next guest. When you are ready to checkout simply dial **47.
  </p>

  <section class="hints">
    <h2 class="hints__title">Helpful Hints:</h2>
    <ul class="hints__list">
      <li class="hint"><svg width="16" height="16" viewBox="0 0 16 16"><path d="M8 1v14M2 4.5l12 7M2 11.5l12-7" stroke="var(--ink)" stroke-width="1.5"/></svg>Turn the lever in the freezer to start making ice</li>
      <li class="hint"><svg width="16" height="16" viewBox="0 0 16 16"><path d="M1 11c2-2 3 0 5 0s3-2 5 0 3 0 4 0M1 14c2-2 3 0 5 0s3-2 5 0 3 0 4 0" stroke="var(--ink)" stroke-width="1.4" fill="none"/></svg>The Waterpark can be accessed from the 1st Floor</li>
      <li class="hint"><svg width="16" height="16" viewBox="0 0 16 16"><circle cx="8" cy="8" r="6.5" stroke="var(--ink)" stroke-width="1.4" fill="none"/><path d="M8 4v4l3 2" stroke="var(--ink)" stroke-width="1.4" fill="none"/></svg>The Indoor Waterpark is open from 9AM to 11PM</li>
      <li class="hint"><svg width="16" height="16" viewBox="0 0 16 16"><rect x="3" y="1" width="10" height="14" rx="1" stroke="var(--ink)" stroke-width="1.4" fill="none"/><path d="M5 4h6M5 7h6M5 12h3" stroke="var(--ink)" stroke-width="1.4"/></svg>Vending with Snacks &amp; Drinks are available on Floors 1, 2, 4, &amp; 5</li>
      <li class="hint"><svg width="16" height="16" viewBox="0 0 16 16"><path d="M8 15s5-5 5-9a5 5 0 0 0-10 0c0 4 5 9 5 9z" stroke="var(--ink)" stroke-width="1.4" fill="none"/><circle cx="8" cy="6" r="1.8" fill="var(--ink)"/></svg>The closest grocery store is Brindlemart</li>
      <li class="hint"><svg width="16" height="16" viewBox="0 0 16 16"><path d="M1 2h2l2 9h8l2-6H4" stroke="var(--ink)" stroke-width="1.4" fill="none"/><circle cx="6" cy="14" r="1.2" fill="var(--ink)"/><circle cx="12" cy="14" r="1.2" fill="var(--ink)"/></svg>You can also conveniently order groceries via Pantrygo from Halvey, Grain Town, &amp; Tamrel</li>
      <li class="hint"><svg width="16" height="16" viewBox="0 0 16 16"><rect x="2" y="5" width="12" height="10" stroke="var(--ink)" stroke-width="1.4" fill="none"/><path d="M5 5a3 3 0 0 1 6 0" stroke="var(--ink)" stroke-width="1.4" fill="none"/></svg>Additional convenience items are available for purchase at the Front Desk</li>
      <li class="hint"><svg width="16" height="16" viewBox="0 0 16 16"><path d="M3 1.5l3 .5 1 3.5-2 1.5a9 9 0 0 0 4 4l1.5-2 3.5 1 .5 3c-6 1-13-6-11.5-11.5z" stroke="var(--ink)" stroke-width="1.3" fill="none"/></svg>Use our Express Checkout by Dialing **47</li>
    </ul>
  </section>

  <footer class="closing">
    <p class="closing__thanks">Thank you so much for choosing the Resort for your Smoky Mountain Vacation!</p>
    <p class="closing__team">The Resort Management Team</p>
  </footer>

  <div class="corner-brand"><span class="corner-brand__mark"></span><span class="corner-brand__name">THE RESORT</span></div>
</article>
</body>
</html>
```